Salmon Shop that sells both wholesale and retail salmon in a variety of ways.

"Tidewater Fishery" is a business that is selling atlantic salmon in every way possible. We will be a salmon butcher to the public for retail purchase and we will also be out and about trying to sell our products to restaurants cafes and any other wholesale way. Our product is from Tasmania but we will be trading on the Sunshine Coast. The shop design has an urban, rustic feel and very much about the product. One of the owners has worked on salmon farms for 15 years and we want it to be very specialised and quality. I have nothing to offer you to help with this design....I would like both a salmon on the card, not sure if image or silohette is best and would like the other side to have a fillet with a tag of some sort. We are looking for a logo also. Use a photo of an Atlantic Salmon, Atlantic Salmon have two fins along the back.
Updates

Project Deadline Extended Reason: I am extending the deadline as I have still not got exactly what I want. All designers have added something great to what I am after and I just need someone to pull it all together. I have put in a new brief with a sketched image to help so we can get this perfect. Please read all the instructions. Thank you Added Monday, February 16, 2015

Target Market(s)

Restaurants, cafes

Industry/Entity Type

Retail

Contact Information for Business Card

Tidewater Fishery (Not to have "Shop" at the end.Shop 12/130-164 Brisbane RdMooloolaba 4557

Colors
1c66ab

Requirements
Must have
• logo for Tidewater Fishery with the S being salmon fillet of fresh salmon on white platemap of tasmaniasepia /black and white image of atlantic salmon
Nice to have
• fillet of salmonmap of tasmaniasalmon
Should not have
• Not Shop at the end.

```html
<!DOCTYPE html>
<html lang="en">
<head>
<meta charset="utf-8">
<title>Tidewater Fishery – Business Cards</title>
<link href="https://fonts.googleapis.com/css2?family=Poppins:wght@700&family=Open+Sans:wght@300;400&display=swap" rel="stylesheet">
<style>
  :root {
    --backdrop: #d9dbdb;
    --card-white: #ffffff;
    --card-red: #c23b27;
    --brand-orange: #e8472a;
    --ink: #3a3a3a;
    --paper-edge: rgba(0, 0, 0, 0.22);
  }
  * { box-sizing: border-box; margin: 0; padding: 0; }
  html, body {
    width: 1200px;
    height: 800px;
    overflow: hidden;
    background: var(--backdrop);
  }
  .stage {
    width: 1200px;
    height: 800px;
    display: flex;
    align-items: center;
    justify-content: center;
    gap: 60px;
  }
  .card {
    width: 520px;
    height: 300px;
    box-shadow: 0 3px 0 var(--paper-edge);
    display: flex;
    flex-direction: column;
    justify-content: center;
    align-items: center;
  }
  .card--front { background: var(--card-white); }
  .card--back { background: var(--card-red); }

  .brand {
    display: flex;
    align-items: center;
    gap: 14px;
  }
  .brand__dot {
    width: 46px;
    height: 46px;
    border-radius: 50%;
    flex: none;
  }
  .wordmark {
    font-family: "Poppins", sans-serif;
    font-weight: 700;
    font-size: 38px;
    line-height: 1;
    letter-spacing: 0.3px;
  }
  .card--front .brand__dot { background: var(--brand-orange); }
  .card--front .wordmark { color: var(--brand-orange); }
  .card--back .brand__dot { background: var(--card-white); }
  .card--back .wordmark { color: var(--card-white); }

  .contact {
    margin-top: 34px;
    font-family: "Open Sans", sans-serif;
    font-style: normal;
    font-weight: 300;
    font-size: 17px;
    line-height: 1.6;
    color: var(--ink);
    text-align: center;
  }
</style>
</head>
<body>
  <main class="stage">
    <section class="card card--front">
      <div class="brand">
        <span class="brand__dot" aria-hidden="true"></span>
        <h1 class="wordmark">Tidewater Fishery</h1>
      </div>
      <address class="contact">
        <p class="contact__address">7/210-238 Kellaway Rd Marlin Bay 4558</p>
        <p class="contact__phone">Call:-0000-000-000</p>
      </address>
    </section>
    <section class="card card--back">
      <div class="brand">
        <span class="brand__dot" aria-hidden="true"></span>
        <p class="wordmark">Tidewater Fishery</p>
      </div>
    </section>
  </main>
</body>
</html>
```